Velmor Glazing

Velmor Glazing company specializing in commercial fit outs, pool fencing, frameless showers and glass splash backs, im after a very young/modern logo, it doesnt have to be revelent to glazing and a classy "boss like" design for the card. thank you in advanced

im thinking carbon fiber back ground or something along that line with bright orange wording or something maybe, open to suggestions 

Fencing

company name, name, phone and products

```html
<!DOCTYPE html>
<html lang="en">
<head>
<meta charset="utf-8">
<title>Velmor Glazing – Business Card</title>
<link rel="stylesheet" href="https://fonts.googleapis.com/css2?family=Exo+2:wght@300;700&family=Roboto+Condensed:wght@700&display=swap">
<style>
  :root {
    --stage: #2a2c2b;
    --card-edge: #050505;
    --weave-light: #4a4a4a;
    --weave-mid: #1e1e1e;
    --weave-dark: #030303;
    --band: rgba(0, 0, 0, 0.62);
    --orange: #f26a23;
    --white: #ffffff;
    --tagline: #e6e6e6;
  }
  * { margin: 0; padding: 0; box-sizing: border-box; }
  html, body { width: 1200px; height: 900px; overflow: hidden; background: var(--stage); }
  .canvas { position: relative; width: 1200px; height: 900px; }

  .card {
    position: absolute;
    top: 293px;
    width: 516px;
    height: 312px;
    background: var(--card-edge);
    overflow: hidden;
  }
  .card--front { left: 71px; }
  .card--back { left: 612px; }

  .weave-backdrop {
    position: absolute;
    inset: 0;
    background: radial-gradient(ellipse 62% 58% at 50% 45%, var(--weave-light) 0%, var(--weave-mid) 50%, var(--weave-dark) 100%);
  }
  .card--back .weave-backdrop {
    background: radial-gradient(ellipse 55% 60% at 50% 52%, var(--weave-light) 0%, var(--weave-mid) 50%, var(--weave-dark) 100%);
  }

  /* Front */
  .wordmark {
    position: absolute;
    left: 0; right: 0;
    top: 150px;
    display: flex;
    justify-content: center;
    align-items: center;
    gap: 12px;
    font-family: "Exo 2", sans-serif;
    font-weight: 700;
    font-size: 42px;
    line-height: 1;
    color: var(--white);
  }
  .wordmark__mark {
    width: 16px; height: 16px;
    background: var(--orange);
  }
  .services {
    position: absolute;
    left: 0; right: 0;
    top: 266px;
    text-align: center;
    font-family: "Exo 2", sans-serif;
    font-weight: 300;
    font-size: 14px;
    letter-spacing: -0.2px;
    color: var(--tagline);
    white-space: nowrap;
  }
  .services__divider { color: var(--orange); padding: 0 2px; }

  /* Back */
  .name-band {
    position: absolute;
    left: 0; right: 0;
    top: 114px;
    height: 85px;
    background: var(--band);
  }
  .contact-block {
    position: absolute;
    left: 112px;
    top: 118px;
    width: 296px;
  }
  .role {
    display: flex;
    align-items: flex-end;
    gap: 4px;
    font-family: "Roboto Condensed", sans-serif;
    font-weight: 700;
    font-size: 15px;
    color: var(--white);
  }
  .role__rule {
    flex: 1;
    height: 1px;
    background: var(--white);
    margin-bottom: 4px;
  }
  .person-name {
    font-family: "Roboto Condensed", sans-serif;
    font-weight: 700;
    font-size: 42px;
    line-height: 40px;
    letter-spacing: 5px;
    color: var(--orange);
    white-space: nowrap;
  }
  .contact-line {
    font-family: "Roboto Condensed", sans-serif;
    font-weight: 700;
    font-size: 15px;
    color: var(--white);
    white-space: nowrap;
    display: flex;
    align-items: center;
    gap: 5px;
  }
  .contact-line__dot {
    width: 5px; height: 5px;
    border-radius: 50%;
    background: var(--orange);
  }
</style>
</head>
<body>
<main class="canvas">
  <section class="card card--front">
    <div class="weave-backdrop" role="img" aria-label="Dark carbon fibre weave texture with a soft central highlight"></div>
    <div class="wordmark">
      <span class="wordmark__mark"></span>
      <span class="wordmark__name">Velmor Glazing</span>
    </div>
    <p class="services">commercial fit outs<span class="services__divider">|</span>pool fencing<span class="services__divider">|</span>frameless showers<span class="services__divider">|</span>glass splash backs</p>
  </section>

  <section class="card card--back">
    <div class="weave-backdrop" role="img" aria-label="Dark carbon fibre weave texture with a soft central highlight"></div>
    <div class="name-band"></div>
    <div class="contact-block">
      <p class="role"><span class="role__rule"></span><span>Managing Director</span></p>
      <h1 class="person-name">DANIEL REYES</h1>
      <p class="contact-line"><span>+63 917 555 0142</span><span class="contact-line__dot"></span><span>www.velmorglazing.com</span></p>
    </div>
  </section>
</main>
</body>
</html>
```